Business card design for a world class martial arts and group fitness facility

We need a professional and eye catching design for a business card. The card will be used in networking as well as marketing.
We are a martial arts facility offering Taekwondo, Brazilian Jiu Jitsu, and group fitness. All of our programs are geared for kids and adults.
Our Taekwondo program is lead by a Hall of Fame instructor who was Instructor of the Year in 2015.
Our Brazilian Jiu Jitsu program is lead by a wold class instructor who is also a part of the renown Brazilian KVO team.
We offer 3 focused group fitness programs: Ring striking, Pulse Fitness, and The Meadow which are all lead by certified instructors in a small group setting.
Our facility is state of the art and has been recognized as such in nationally published magazines.
Our business is named The Lantern which is the linear logo that is attached. This is the main logo. I also attached a circular logo we have used in some marketing material. Our Jiu Jitsu program is the KVO team logo. The Taekwondo program is the TORVEX Prime. It would be nice to somehow incorporate all 3 logos, but The Lantern is most important.
Industry/Entity Type
Martial Art
Contact Information for Business Card
We would like to use all 3 logos if possible but The Lantern is the most important. We would like to have a place for a staff member's name while keeping the focus on the programs we offer.
Look and feel
Each slider illustrates characteristics of the customer's brand and the style your logo design should communicate.

```html
<!DOCTYPE html>
<html lang="en">
<head>
<meta charset="utf-8">
<title>The Lantern – Business Card</title>
<link rel="stylesheet" href="https://fonts.googleapis.com/css2?family=Open+Sans:wght@400;800&display=swap">
<style>
  :root {
    --backdrop: #9a9a9a;
    --card: #fbfbfb;
    --ink: #1a1a1a;
    --brick: #8b3a22;
    --band: #0c0a0a;
    --signal: #c8232c;
    --white: #ffffff;
  }
  * { margin: 0; padding: 0; box-sizing: border-box; }
  html, body {
    width: 1200px; height: 1121px; overflow: hidden;
    background: var(--backdrop);
    font-family: "Open Sans", Arial, sans-serif;
  }
  .card {
    position: absolute; left: 255px; width: 697px; height: 415px;
    background: var(--card);
    box-shadow: 0 6px 18px rgba(0,0,0,0.25);
    overflow: hidden;
  }
  .card--front { top: 98px; }
  .card--back { top: 600px; }

  .brand {
    position: absolute; left: 0; right: 0;
    display: flex; justify-content: center; align-items: center; gap: 14px;
    font-weight: 800; font-size: 62px; letter-spacing: 1px;
    color: var(--ink); text-transform: uppercase; line-height: 1;
  }
  .brand__mark { width: 26px; height: 26px; background: var(--brick); }
  .card--front .brand { top: 56px; }
  .card--back .brand { top: 250px; }

  .swoosh { position: absolute; inset: 0; width: 697px; height: 415px; }

  .contact { position: absolute; left: 89px; top: 254px; list-style: none; }
  .contact__item {
    display: flex; align-items: center; gap: 16px;
    font-size: 18px; color: var(--ink); height: 25px;
  }
  .contact__icon { width: 14px; height: 14px; }
  .divider {
    position: absolute; left: 402px; top: 205px;
    width: 1.5px; height: 150px; background: var(--ink);
  }
  .staff-name {
    position: absolute; left: 456px; top: 205px;
    font-size: 23px; color: var(--brick);
  }

  .program-band {
    position: absolute; left: 0; top: 0; width: 697px; height: 204px;
    background: var(--band);
  }
  .program {
    position: absolute; top: 0; height: 204px;
    display: flex; align-items: center; gap: 12px;
    color: var(--white); font-weight: 800; text-transform: uppercase;
  }
  .program--taekwondo { left: 96px; font-size: 34px; }
  .program--jiujitsu { left: 462px; font-size: 38px; }
  .program__dot { width: 22px; height: 22px; border-radius: 50%; background: var(--signal); }
</style>
</head>
<body>

<section class="card card--front">
  <div class="brand"><span class="brand__name">The Lantern</span><span class="brand__mark"></span></div>

  <svg class="swoosh" viewBox="0 0 697 415" aria-hidden="true">
    <path d="M0,376 C220,368 470,330 697,250 L697,262 C480,350 240,398 0,404 Z" fill="var(--ink)"/>
    <path d="M330,415 C480,400 610,352 697,276 L697,415 Z" fill="var(--brick)"/>
  </svg>

  <ul class="contact">
    <li class="contact__item">
      <svg class="contact__icon" viewBox="0 0 14 14" aria-hidden="true"><rect width="14" height="14" fill="var(--brick)"/><rect x="4.5" y="2.5" width="5" height="9" rx="1" fill="none" stroke="#fff" stroke-width="1.2"/></svg>
      <span>425-555-0148</span>
    </li>
    <li class="contact__item">
      <svg class="contact__icon" viewBox="0 0 14 14" aria-hidden="true"><rect width="14" height="14" fill="var(--brick)"/><circle cx="7" cy="7" r="4" fill="none" stroke="#fff" stroke-width="1.2"/><line x1="3" y1="7" x2="11" y2="7" stroke="#fff" stroke-width="1"/></svg>
      <span>www.danawhitlow.com</span>
    </li>
    <li class="contact__item">
      <svg class="contact__icon" viewBox="0 0 14 14" aria-hidden="true"><rect width="14" height="14" fill="var(--brick)"/><rect x="3" y="4" width="8" height="6" fill="none" stroke="#fff" stroke-width="1.1"/><path d="M3,4 L7,7.5 L11,4" fill="none" stroke="#fff" stroke-width="1.1"/></svg>
      <span>danawhitlow@mailbox.com</span>
    </li>
  </ul>

  <div class="divider"></div>
  <p class="staff-name">Dana Whitlow</p>
</section>

<section class="card card--back">
  <div class="program-band">
    <div class="program program--taekwondo"><span>TORVEX Prime</span></div>
    <div class="program program--jiujitsu"><span class="program__dot"></span><span>KVO</span></div>
  </div>
  <div class="brand"><span class="brand__name">The Lantern</span><span class="brand__mark"></span></div>
</section>

</body>
</html>
```